Website - Varsity Homehelpers
Varsity Homehelpers
Project: Website - Varsity Homehelpers
Website - Varsity Homehelpers - Personal Care
Creative Brief
Personal Care
www.varsityhomehelpers-example.com
Varsity Homehelpers is a student based non-medical home health care company designed to enable our clients to age safely in their own homes, while helping prepare our workers for successful careers as healthcare professionals. Our services include: Assistance with activities of daily living, medication management, hygiene monitoring, housekeeping, cooking, transportation, shopping, and companionship. The workplace is our client’s homes, where they feel safe and comfortable. Clients are cared for by college students who are studying to become future Registered Nurses, Physicians, Surgeons, Therapists, Pharmacists, Dietitians, and more. This is a rare opportunity for our clients to be cared for by highly educated and respectable individuals at a rate our competitors can not match for the service. Varsity Homehelpers was created to help our workers meet the financial demands of higher education while creating a solid foundation for professional careers in the health care industry, by enabling our clients to be more then just a patient, but also a teacher!
I would like images of: College students, graduating students, young health care professionals (doctors, nurses, ect) and active healthier looking seniors. I do not want images of seniors in wheelchairs, with walkers, or that appear as if the need help.
below header
www.dorvantix-example.com
www.quellbrook-example.com
www.fernwaymeridianholdings-example.com
The business is a combination of website url 1 & 2. I would like to incorporate concepts from both of these into my website. Has to compete in professionalism and attractiveness. I do really like the simple layout of url 3 as well though. Please use your imagination and good luck!

```html
<!DOCTYPE html>
<html lang="en">
<head>
<meta charset="utf-8">
<title>Varsity Homehelpers – Personal Care</title>
<link href="https://fonts.googleapis.com/css2?family=PT+Sans:wght@400;700&family=PT+Sans+Narrow:wght@400;700&display=swap" rel="stylesheet">
<style>
:root{
  --page-bg:#e3e5e8;
  --sheet:#ffffff;
  --red:#c9161d;
  --red-dark:#9d0f14;
  --navy:#1c3a6b;
  --navy-deep:#15294d;
  --sky:#d7e9f4;
  --text:#4a4a4a;
  --muted:#8a8f96;
  --line:#d9dde2;
  --panel:#f2f3f5;
}
*{box-sizing:border-box;margin:0;padding:0}
html,body{width:1200px;height:1099px;overflow:hidden}
body{background:var(--page-bg);font-family:"PT Sans",Arial,sans-serif;color:var(--text);position:relative}
.sheet{position:absolute;left:170px;top:0;width:860px;height:1075px;background:var(--sheet);box-shadow:0 0 8px rgba(0,0,0,.12)}

/* header */
.brand{position:absolute;left:14px;top:18px;display:flex;align-items:center;gap:10px}
.brand-dot{width:22px;height:22px;border-radius:50%;background:var(--red)}
.brand-name{font-family:"PT Sans",Arial,sans-serif;font-weight:700;font-size:30px;color:var(--red);letter-spacing:-.5px}
.account-bar{position:absolute;right:30px;top:0;height:30px;width:250px;background:var(--navy);display:flex;align-items:center;gap:6px;padding:0 10px;border-radius:0 0 4px 4px}
.social{width:14px;height:14px;background:#5d7fb3;border-radius:2px}
.account-links{margin-left:auto;color:#fff;font-size:11px}
.call{position:absolute;right:30px;top:40px;font-size:17px;color:var(--navy)}

.main-nav{position:absolute;left:0;top:113px;width:860px;height:40px;background:linear-gradient(#d8242a,var(--red-dark));display:flex}
.main-nav a{color:#fff;text-decoration:none;font-size:15px;padding:0 18px;line-height:40px;border-right:1px solid rgba(255,255,255,.25)}
.main-nav a.active{background:var(--red-dark)}

/* hero */
.hero{position:absolute;left:10px;top:164px;width:840px;height:262px;background:var(--sky);overflow:hidden}
.hero-photo{position:absolute;left:0;top:0;width:430px;height:262px;background:linear-gradient(120deg,#a9c9db,#e9d2bf 55%,#c9dde6)}
.hero-copy{position:absolute;left:455px;top:42px;width:350px}
.hero-copy h1{font-weight:400;font-size:34px;line-height:40px;color:var(--navy)}
.hero-copy p{margin-top:12px;font-size:12px;line-height:16px;color:#333}
.dots{position:absolute;right:18px;bottom:16px;display:flex;gap:6px}
.dots span{width:14px;height:14px;border-radius:50%;background:#6b90c0}
.dots span.on{background:var(--navy)}

/* feature boxes */
.features{position:absolute;left:10px;top:441px;width:840px;height:125px;display:flex;gap:10px}
.feature{flex:1;position:relative;border:1px solid var(--line);background:linear-gradient(#fff,#f3f5f8);padding:8px 10px}
.feature h2{font-family:"PT Sans Narrow",Arial,sans-serif;font-weight:700;font-size:24px;color:var(--navy)}
.feature p{width:140px;font-size:11px;line-height:14px;margin-top:4px}
.feature .thumb{position:absolute;right:8px;top:14px;width:110px;height:100px;background:linear-gradient(#cfe0ec,#e8dccf)}
.btn{display:inline-block;margin-top:8px;background:var(--navy);color:#fff;font-size:12px;font-weight:700;padding:5px 10px;border-radius:3px}

/* welcome */
.welcome{position:absolute;left:10px;top:578px;width:840px}
.welcome h2{font-family:"PT Sans Narrow",Arial,sans-serif;font-weight:700;font-size:24px;color:var(--navy);padding-bottom:8px;border-bottom:1px solid var(--line)}
.welcome p{margin-top:10px;font-size:13px;line-height:19px;color:#555}

/* tabs */
.tabs{position:absolute;left:10px;top:742px;width:560px;height:245px;border:1px solid var(--line);background:var(--panel)}
.tab-row{display:flex;height:36px;background:#fff;border-bottom:1px solid var(--line)}
.tab-row span{flex:1;text-align:center;line-height:36px;font-size:13px;font-weight:700;color:var(--navy)}
.tab-row span.active{border:1px solid var(--line);border-bottom:1px solid var(--panel);background:var(--panel)}
.tab-body{position:relative;padding:16px}
.tab-photo{position:absolute;left:16px;top:16px;width:150px;height:105px;background:linear-gradient(#e6d6c4,#c8d8e2)}
.tab-text{margin-left:170px}
.tab-text h3{font-size:13px;line-height:17px;color:#333}
.tab-text p{margin-top:6px;font-size:11px;line-height:15px;color:#666}

.videos{position:absolute;left:582px;top:742px;width:268px}
.videos h2{font-family:"PT Sans Narrow",Arial,sans-serif;font-weight:700;font-size:24px;color:var(--navy)}
.player{margin-top:6px;width:268px;height:200px;border:1px solid var(--line);background:#222;position:relative}
.player-frame{position:absolute;left:4px;top:4px;right:4px;bottom:24px;background:linear-gradient(100deg,#7fa3bf,#d9c4b0)}
.player svg{position:absolute;left:112px;top:68px}
.player-bar{position:absolute;left:0;right:0;bottom:0;height:22px;background:#333;display:flex;align-items:center;padding:0 8px;gap:8px}
.player-bar i{display:block;flex:1;height:4px;background:#777}

.footer-nav{position:absolute;left:10px;top:1013px;width:840px;height:36px;background:linear-gradient(#d8242a,var(--red-dark));display:flex;padding-left:20px}
.footer-nav a{color:#fff;text-decoration:none;font-size:11px;line-height:36px;padding:0 22px}
</style>
</head>
<body>
<div class="sheet">
  <header>
    <div class="brand"><span class="brand-dot"></span><span class="brand-name">Varsity Homehelpers</span></div>
    <div class="account-bar">
      <span class="social"></span><span class="social"></span><span class="social"></span>
      <span class="account-links">LOG IN | SIGN UP | Help</span>
    </div>
    <div class="call">Call Us Today: 1800.555.0142</div>
    <nav class="main-nav">
      <a class="active" href="#">Home</a><a href="#">About Us</a><a href="#">Services</a><a href="#">New &amp; Events</a><a href="#">Contact Us</a>
    </nav>
  </header>

  <section class="hero">
    <div class="hero-photo" role="img" aria-label="Smiling senior woman embracing a young caregiver outdoors"></div>
    <div class="hero-copy">
      <h1>Be more then just a patient, but also a teacher!</h1>
      <p>Lorem ipsum dolor sit amet, consectetur adipiscing elit, sed do eiusmod tempor incididunt ut labore et dolore magna aliqua. Ut enim ad minim veniam. Excepteur sint.</p>
    </div>
    <div class="dots"><span class="on"></span><span></span><span></span></div>
  </section>

  <section class="features">
    <div class="feature">
      <h2>About Us</h2>
      <p>Lorem ipsum dolor sit amet, consectetur adipiscing elit, sed do eiusmod tempor.</p>
      <span class="btn">Learn More</span>
      <div class="thumb" role="img" aria-label="Student caregiver assisting a senior client"></div>
    </div>
    <div class="feature">
      <h2>Clients</h2>
      <p>Lorem ipsum dolor sit amet, consectetur adipiscing elit, sed do eiusmod tempor.</p>
      <span class="btn">Get Started</span>
      <div class="thumb" role="img" aria-label="Active senior couple smiling"></div>
    </div>
    <div class="feature">
      <h2>Students</h2>
      <p>Lorem ipsum dolor sit amet, consectetur adipiscing elit, sed do eiusmod tempor.</p>
      <span class="btn">Apply Now</span>
      <div class="thumb" role="img" aria-label="Young nurse in blue scrubs"></div>
    </div>
  </section>

  <section class="welcome">
    <h2>Welcome to Varsity Homehelpers</h2>
    <p>Varsity Homehelpers is a student based non-medical home health care company designed to enable our clients to age safely in their own homes, while helping prepare our workers for successful careers as healthcare professionals. Our services include: Assistance with activities of daily living, medication management, hygiene monitoring, housekeeping, cooking, transportation, shopping, and companionship. The workplace is our client's homes, where they feel safe and comfortable.</p>
  </section>

  <section class="tabs">
    <div class="tab-row"><span class="active">About Us</span><span>Mission</span><span>Photos</span><span>Services</span><span>Contact Us</span></div>
    <div class="tab-body">
      <div class="tab-photo" role="img" aria-label="Young hand holding an older hand"></div>
      <div class="tab-text">
        <h3>Lorem ipsum dolor sit amet, consectetur adipiscing elit, sed do eiusmod tempor incididunt ut labore et</h3>
        <p>Curabitur sed urna id nunc pulvinar semper. Nunc sit amet tortor sit amet lacus sagittis posuere cursus vitae. Curabitur sed urna id nunc pulvinar semper. Nunc sit amet tortor sit amet lacus sagittis posuere cursus vitae. Curabitur sed urna id nunc pulvinar semper. Nunc sit amet tortor sit amet lacus sagittis.</p>
      </div>
    </div>
  </section>

  <section class="videos">
    <h2>Videos</h2>
    <div class="player">
      <div class="player-frame" role="img" aria-label="Video still of a caregiver with a senior client"></div>
      <svg width="44" height="44" viewBox="0 0 44 44"><circle cx="22" cy="22" r="20" fill="rgba(255,255,255,.8)"/><path d="M17 13 L32 22 L17 31 Z" fill="#1c3a6b"/></svg>
      <div class="player-bar"><svg width="10" height="10" viewBox="0 0 10 10" style="position:static"><path d="M1 0 L10 5 L1 10 Z" fill="#ddd"/></svg><i></i></div>
    </div>
  </section>

  <nav class="footer-nav">
    <a href="#">Home</a><a href="#">Company</a><a href="#">Products</a><a href="#">Support</a><a href="#">Contact Us</a>
  </nav>
</div>
</body>
</html>
```